occupational hygiene card design

We supply a service to the resource sector, commercial or government organisations to access health risks from physical or chemical hazards. We are a technical discipline that works within legislation.

Industry/Entity Type

Government

Contact Information for Business Card

KPLA
Kestrel plains occupational hygiene

```html
<!DOCTYPE html>
<html lang="en">
<head>
<meta charset="utf-8">
<title>KPLA – Business Card</title>
<link rel="stylesheet" href="https://fonts.googleapis.com/css2?family=Nanum+Gothic:wght@400;800&family=Libre+Baskerville:wght@400&display=swap">
<style>
  :root {
    --paper: #efeeee;
    --lime: #a8cf0f;
    --ink: #5a5050;
    --rule: #b9b9b9;
  }
  html, body {
    margin: 0;
    padding: 0;
    width: 1200px;
    height: 720px;
    overflow: hidden;
    background: var(--paper);
  }
  .card {
    position: relative;
    width: 1200px;
    height: 720px;
    background: var(--paper);
    font-family: "Nanum Gothic", sans-serif;
    color: var(--ink);
  }
  .card__corners {
    position: absolute;
    inset: 0;
  }
  .corner { fill: var(--lime); }

  .brand {
    position: absolute;
    left: 80px;
    top: 100px;
    width: 368px;
  }
  .brand__name {
    display: block;
    font-family: "Nanum Gothic", sans-serif;
    font-weight: 800;
    font-size: 94px;
    line-height: 1;
    letter-spacing: 10px;
    color: var(--ink);
  }
  .brand__rule {
    height: 1px;
    background: var(--rule);
    margin-top: 2px;
  }
  .brand__tagline {
    font-family: "Libre Baskerville", serif;
    font-size: 11.5px;
    letter-spacing: 1.6px;
    color: #1e1e2a;
    margin-top: 4px;
    white-space: nowrap;
  }

  .contact {
    position: absolute;
    left: 950px;
    top: 490px;
  }
  .contact__address {
    font-size: 24px;
    margin: 0 0 16px;
    font-weight: 400;
  }
  .contact__list {
    margin: 0;
    padding: 0;
    list-style: none;
    font-size: 15px;
    line-height: 23px;
  }
  .contact__label {
    display: inline-block;
    width: 38px;
  }
  .contact__sep {
    display: inline-block;
    width: 13px;
  }
  .contact__indent { padding-left: 51px; }
</style>
</head>
<body>
<main class="card">
  <svg class="card__corners" width="1200" height="720" viewBox="0 0 1200 720" aria-hidden="true">
    <polygon class="corner" points="939,0 1200,0 1200,261 1140,203 1140,60 997,60"/>
    <polygon class="corner" points="0,459 60,517 60,660 203,660 262,720 0,720"/>
  </svg>

  <header class="brand">
    <span class="brand__name">KPLA</span>
    <div class="brand__rule"></div>
    <div class="brand__tagline">KESTREL PLAINS OCCUPATIONAL HYGIENE</div>
  </header>

  <section class="contact">
    <h2 class="contact__address">Your Address</h2>
    <ul class="contact__list">
      <li><span class="contact__label">tel</span><span class="contact__sep">:</span><span class="contact__value">08 5550 1234</span></li>
      <li><span class="contact__label">fax</span><span class="contact__sep">:</span><span class="contact__value">08 5550 1299</span></li>
      <li class="contact__indent"><span class="contact__value">info@kplaoh.com</span></li>
    </ul>
  </section>
</main>
</body>
</html>
```